Biz Card & Stationary for Kids Indoor Play Space Company
Bramble Hollow
Biz Card & Stationary for Kids Indoor Play Space Company - Childcare
Creative Brief
Bright & Fun-filled
Marla Quint
Owner
7148 Garnet Ave. Ashbury Falls, OH 44712
marla.quint@bramblehollowplay.com
https://bramblehollowplay.com/
Would like the feel of the design to be consistent with our website. I will upload our logo. I will provide you with a biz phone # in a few days. If needed, our Logo Font is "Brady Bunch Remastered".
zestlark zestlark
1. In addition to biz cards design, we also want stationary design (letterhead and envelope). 2. We would like to see versions where our logo has a different tag line of "Indoor Play Center". Maybe this tag-line could be used on the front of the card and the original tag-line on the back of the card?

```html
<!DOCTYPE html>
<html lang="en">
<head>
<meta charset="utf-8">
<title>Bramble Hollow – Business Card</title>
<link rel="stylesheet" href="https://fonts.googleapis.com/css2?family=Fredoka:wght@500;600&family=Open+Sans:wght@400;600;700&display=swap">
<style>
  :root {
    --red: #e11d2b;
    --blue: #1f5fb8;
    --white: #ffffff;
    --ink: #3a3a3a;
    --backdrop: #e9e9ec;
    --photo-a: #d9c7b0;
    --photo-b: #9fb6c9;
    --social-1: #7b3fa0;
    --social-2: #1f8fe0;
    --social-3: #e0457b;
  }
  * { margin: 0; padding: 0; box-sizing: border-box; }
  html, body { width: 1200px; height: 961px; overflow: hidden; background: var(--backdrop); }
  body { position: relative; font-family: "Open Sans", sans-serif; }

  .card {
    position: absolute; left: 232px; width: 736px; height: 420px;
    overflow: hidden; background: var(--white);
    box-shadow: 0 6px 18px rgba(0,0,0,.18);
  }
  .card--front { top: 40px; }
  .card--back { top: 500px; }

  /* front */
  .photo {
    position: absolute; inset: 0;
    background: linear-gradient(135deg, var(--photo-a) 0%, #e8ddd0 45%, var(--photo-b) 100%);
  }
  .cloud-panel { position: absolute; right: 0; bottom: 0; width: 520px; height: 250px; }
  .social { position: absolute; right: 40px; top: 200px; display: flex; gap: 8px; list-style: none; }
  .social li { width: 24px; height: 24px; border-radius: 50%; }
  .social .s1 { background: var(--social-1); }
  .social .s2 { background: var(--social-2); }
  .social .s3 { background: var(--social-3); }
  .front-web {
    position: absolute; right: 40px; top: 238px;
    font-weight: 700; font-size: 15px; color: var(--red);
  }
  .front-brand { position: absolute; right: 40px; bottom: 38px; text-align right; text-align: right; }
  .brand-name {
    font-family: "Fredoka", sans-serif; font-weight: 600; color: var(--red);
    font-size: 52px; line-height: 1; letter-spacing: .5px;
  }
  .front-tagline {
    font-family: "Fredoka", sans-serif; font-weight: 500; color: var(--blue);
    font-size: 22px; margin-top: 6px;
  }

  /* back */
  .back-brand { position: absolute; top: 70px; left: 0; right: 0; text-align: center; }
  .back-brand .brand-name { font-size: 60px; }
  .back-tagline {
    font-family: "Fredoka", sans-serif; font-weight: 500; color: var(--blue);
    font-size: 24px; margin-top: 4px;
  }
  .back-bands { position: absolute; left: 0; bottom: 0; width: 736px; height: 230px; }
  .stripe-name { font-family: "Fredoka", sans-serif; font-weight: 600; font-size: 12px; fill: var(--blue); }
  .holder { position: absolute; left: 36px; bottom: 34px; color: var(--white); }
  .holder-name { font-weight: 700; font-size: 24px; }
  .holder-role { font-size: 15px; margin: 2px 0 6px; }
  .holder-address { font-size: 15px; line-height: 1.35; font-style: normal; }
  .contacts {
    position: absolute; right: 30px; bottom: 34px; list-style: none;
    color: var(--white); font-size: 13.5px;
  }
  .contacts li { display: flex; align-items: center; gap: 8px; line-height: 1.75; }
  .contacts svg { width: 13px; height: 13px; flex: none; }
</style>
</head>
<body>

<section class="card card--front">
  <div class="photo" role="img" aria-label="Photo of children playing with toys in a bright indoor play room"></div>
  <svg class="cloud-panel" viewBox="0 0 520 250" preserveAspectRatio="none" aria-hidden="true">
    <path d="M0 250 L0 150 Q20 110 60 120 Q80 80 125 95 Q150 60 195 80 Q225 45 270 65 Q300 30 345 50 Q370 15 415 30 Q445 0 485 15 Q505 5 520 10 L520 250 Z" fill="#ffffff"/>
  </svg>
  <ul class="social" aria-label="Social media links">
    <li class="s1"></li>
    <li class="s2"></li>
    <li class="s3"></li>
  </ul>
  <div class="front-web">www.bramblehollowplay.com</div>
  <div class="front-brand">
    <div class="brand-name">Bramble Hollow</div>
    <div class="front-tagline">Where Imagination Plays</div>
  </div>
</section>

<section class="card card--back">
  <div class="back-brand">
    <div class="brand-name">Bramble Hollow</div>
    <div class="back-tagline">Indoor Play Center</div>
  </div>
  <svg class="back-bands" viewBox="0 0 736 230" aria-hidden="true">
    <polygon points="0,70 20,68.64 20,82.64 0,84" fill="var(--blue)"/>
    <polygon points="130,61.17 736,20 736,34 130,75.17" fill="var(--blue)"/>
    <text class="stripe-name" x="27" y="73" transform="rotate(-3.89 27 73)">Bramble Hollow</text>
    <polygon points="0,90 736,40 736,230 0,230" fill="var(--red)"/>
  </svg>
  <div class="holder">
    <div class="holder-name">Marla Quint</div>
    <div class="holder-role">Owner</div>
    <address class="holder-address">7148 Garnet Ave.<br>Ashbury Falls, OH 44712</address>
  </div>
  <ul class="contacts">
    <li><svg viewBox="0 0 16 16"><path d="M3 1h3l1.5 4-2 1.5a9 9 0 0 0 4 4L11 8.5l4 1.5v3a2 2 0 0 1-2 2A13 13 0 0 1 1 3a2 2 0 0 1 2-2z" fill="#fff"/></svg>555-204-7781</li>
    <li><svg viewBox="0 0 16 16"><rect x="4" y="1" width="8" height="14" rx="1.5" fill="#fff"/><rect x="5.5" y="3" width="5" height="8" fill="#e11d2b"/></svg>555-318-0462</li>
    <li><svg viewBox="0 0 16 16"><rect x="1" y="3" width="14" height="10" rx="1" fill="#fff"/><path d="M1.5 3.5 8 9l6.5-5.5" stroke="#e11d2b" stroke-width="1.4" fill="none"/></svg>marla.quint@bramblehollowplay.com</li>
    <li><svg viewBox="0 0 16 16"><circle cx="8" cy="8" r="6.5" stroke="#fff" stroke-width="1.4" fill="none"/><ellipse cx="8" cy="8" rx="2.8" ry="6.5" stroke="#fff" stroke-width="1.2" fill="none"/><path d="M1.5 8h13" stroke="#fff" stroke-width="1.2"/></svg>www.bramblehollowplay.com</li>
  </ul>
</section>

</body>
</html>
```